A.I. technology startup needs a website design

We need a website design for our artificial intelligence product vkMender.
vkMender is a platform that uses the latest advances in natural language processing and machine learning to intelligently communicate to users and provide users an interface to interact with organizations through natural language. It is designed as a contact centre robot that automates the handling of customer service inquiries, thus helping to improve service quality and reduce operational expenses. Unlike any other artificial intelligence, this system is trained by using a knowledgebase combined with on-the-job training to quickly learn answers to frequently asked questions and be able to provide intelligent responses to user inquiries.
We would like this product website to show prospective customers what vkMender is about and to generate excitement for this product, as we are in the middle of launching out worldwide.
----------------------------------------------
The website design should be modern and clean. Our product uses cutting edge technology and we want the website to deliver this message.
We like modern style websites with large fonts and images and dynamic design.
There should be a menu at the top with the following options which will navigate the user to the appropriate page:
- vkMender (this acts as the home page)
- Benefits
- How It Works
- About Us
The website should be responsive for mobile device users.
Here are some examples of website designs we like:
http://www.plumvaro.com/
https://www.quillharborinc.com
https://www.bravolume.com/customer-support-software
https://www.fintorra.com/
We have some attachments which may help in the website. Please take a look at our existing material, which includes: vkMender logo, vkMender powerpoint presentation (contains alot of content we can re-use on the website), and more.
Appreciate your creative talent and website expertise, and we look forward to seeing your designs!

```html
<!DOCTYPE html>
<html lang="en">
<head>
<meta charset="utf-8">
<title>vkMender – AI Contact Centre Robot</title>
<link href="https://fonts.googleapis.com/css2?family=Montserrat:wght@400;500;600;700&family=Open+Sans:wght@400;600;700&display=swap" rel="stylesheet">
<style>
:root{
  --blue:#1b7fc6;
  --blue-dark:#125f9c;
  --hero-a:#3a53b8;
  --hero-b:#5a7de0;
  --cyan:#3fc6e6;
  --cyan-icon:#27a8df;
  --ink:#2b2b2b;
  --muted:#6d6d6d;
  --gray-seg:#9a9a9a;
  --gray-bg:#e9e9e9;
  --footer:#1e1e1e;
  --footer-bar:#171717;
  --white:#fff;
}
*{box-sizing:border-box;margin:0;padding:0}
html,body{width:1200px;height:3766px;overflow:hidden}
body{font-family:"Open Sans",sans-serif;color:var(--ink);background:var(--white);position:relative}
.abs{position:absolute}
h1,h2,h3{font-family:"Montserrat",sans-serif}

/* header */
.site-header{position:absolute;left:0;top:0;width:1200px;height:105px;background:var(--white);box-shadow:0 1px 6px rgba(0,0,0,.08);z-index:3}
.brand{position:absolute;left:96px;top:30px;display:flex;align-items:center;gap:12px}
.brand-dot{width:44px;height:44px;border-radius:50%;background:var(--blue)}
.brand-name{font-family:"Montserrat",sans-serif;font-weight:600;font-size:32px;color:var(--blue)}
.main-nav{position:absolute;left:502px;top:42px;display:flex;gap:0;font-size:15px}
.main-nav a{color:#333;text-decoration:none;position:relative}
.main-nav a.active{color:var(--blue)}
.main-nav a.active::after{content:"";position:absolute;left:50%;top:52px;margin-left:-8px;border:8px solid transparent;border-top-color:var(--white)}
.nav-search{position:absolute;left:1082px;top:44px}

/* hero */
.hero{position:absolute;left:0;top:105px;width:1200px;height:598px;background:linear-gradient(100deg,var(--hero-a) 0%,#4565c9 45%,var(--hero-b) 100%);clip-path:polygon(0 0,100% 0,100% 100%,0 89%)}
.hero-art{position:absolute;left:400px;top:70px;width:770px;height:520px;background:radial-gradient(ellipse at 55% 50%,#e8edf6 0%,#b9c4dc 35%,rgba(120,140,200,.35) 65%,rgba(90,120,210,0) 80%)}
.hero-title{position:absolute;left:98px;top:178px;color:var(--white);font-size:40px;font-weight:700;letter-spacing:1px}
.hero-text{position:absolute;left:98px;top:240px;width:340px;color:#e8ecff;font-size:13px;line-height:20px}
.btn-read{position:absolute;left:98px;top:318px;width:122px;height:32px;background:var(--cyan-icon);color:var(--white);font-size:11.5px;font-weight:700;line-height:32px;text-align:center;border-radius:2px}
.hero-dots{position:absolute;left:98px;top:383px;display:flex;gap:9px;align-items:center}
.hero-dots span{width:9px;height:9px;border-radius:50%;background:var(--white)}
.hero-dots span.on{width:15px;height:15px;border:2px solid var(--white);background:transparent;position:relative}
.hero-dots span.on::after{content:"";position:absolute;left:3px;top:3px;width:5px;height:5px;border-radius:50%;background:var(--white)}

/* welcome */
.welcome-title{position:absolute;left:0;top:748px;width:1200px;text-align:center;font-size:44px;font-weight:400;color:#333}
.welcome-title span{color:var(--blue)}
.divider{position:absolute;left:480px;top:812px;width:240px;height:20px}
.welcome-text{position:absolute;left:140px;top:856px;width:920px;text-align:center;font-size:12.5px;line-height:21px;color:#555}
.feature{position:absolute;top:988px;width:320px}
.feature-icon{position:absolute;left:0;top:0;width:80px;height:80px;border-radius:50%;background:var(--cyan-icon)}
.feature-icon svg{position:absolute;left:20px;top:20px}
.feature h3{position:absolute;left:108px;top:2px;width:220px;font-family:"Open Sans",sans-serif;font-weight:400;font-size:16px;line-height:21px;color:#333}
.feature p{position:absolute;left:108px;top:52px;width:200px;font-size:11.5px;line-height:19px;color:#777}

/* where */
.where{position:absolute;left:0;top:1197px;width:1200px;height:506px;background:var(--cyan)}
.where-art{position:absolute;left:640px;top:40px;width:540px;height:466px;background:radial-gradient(ellipse at 55% 55%,#ad3b7d 0%,#7a4a9e 28%,#5f9bd6 55%,rgba(63,198,230,0) 78%)}
.where h2{position:absolute;left:105px;top:100px;color:var(--white);font-size:34px;font-weight:600;line-height:40px}
.where p{position:absolute;left:105px;width:480px;color:#f3fcff;font-size:12px;line-height:19px}
.where ul{position:absolute;left:105px;top:311px;list-style:none;color:var(--white);font-size:12px;font-weight:600}
.where li{height:22.5px;display:flex;align-items:center;gap:14px}
.where li i{width:10px;height:10px;border-radius:50%;background:var(--white)}

/* advantages */
.adv-title{position:absolute;left:0;top:1786px;width:1200px;text-align:center;font-size:30px;font-weight:500;color:#222}
.adv-sub{position:absolute;left:300px;top:1832px;width:600px;text-align:center;font-size:13px;line-height:22px;color:#555}
.adv-item{position:absolute;width:240px}
.adv-item h3{font-family:"Open Sans",sans-serif;font-weight:400;font-size:16.5px;line-height:21px;color:#222;margin-bottom:8px}
.adv-item p{font-size:11px;line-height:19px;color:#666}
.adv-item.left{left:98px;text-align:right}
.adv-item.right{left:878px;text-align:left}
.adv-diagram{position:absolute;left:360px;top:1870px}

/* benefits */
.benefits{position:absolute;left:0;top:2405px;width:1200px;height:545px;background:linear-gradient(180deg,#dedede,#f1f1f1);clip-path:ellipse(110% 100% at 50% 0%)}
.benefits h2{position:absolute;left:0;top:62px;width:1200px;text-align:center;font-size:30px;font-weight:600;color:#222}
.card{position:absolute;top:143px;width:240px;height:252px;background:var(--white);box-shadow:0 2px 6px rgba(0,0,0,.1)}
.card-img{width:240px;height:170px}
.card p{padding:14px 18px 0;text-align:center;font-size:13.5px;line-height:19px;color:#333}

/* speed */
.speed-art{position:absolute;left:150px;top:3012px;width:410px;height:282px;background:linear-gradient(180deg,#3a3a3a,#222);border-radius:18px}
.speed h2{position:absolute;left:610px;top:3043px;color:var(--blue);font-size:30px;font-weight:500;line-height:36px}
.speed p{position:absolute;left:610px;top:3136px;width:470px;font-size:12px;line-height:20px;color:#555}
.speed ul{position:absolute;left:612px;top:3202px;list-style:none;font-size:13px;color:#333}
.speed li{height:24px;display:flex;align-items:center;gap:14px}
.speed li i{width:11px;height:11px;border-radius:50%;background:#333}

/* footer */
.site-footer{position:absolute;left:0;top:3389px;width:1200px;height:301px;background:var(--footer);color:#ddd}
.foot-brand{position:absolute;left:96px;top:92px;display:flex;align-items:center;gap:12px}
.foot-brand .brand-dot{width:54px;height:54px;background:var(--cyan-icon)}
.foot-brand .brand-name{color:var(--cyan-icon);font-size:26px}
.foot-col{position:absolute;top:64px}
.foot-col h3{font-size:16px;font-weight:600;color:var(--white);letter-spacing:.5px;margin-bottom:26px}
.foot-col p,.foot-col li{font-size:12px;line-height:20px;color:#cfcfcf}
.contact-line{display:flex;align-items:center;gap:14px;margin-top:10px}
.news-input{width:245px;height:40px;background:var(--white);margin-top:16px;font-size:11px;color:#777;padding:12px 10px}
.news-btn{width:120px;height:34px;background:var(--blue);color:var(--white);font-size:12px;font-weight:600;text-align:center;line-height:34px;margin-top:10px}
.quick li{list-style:none;display:flex;align-items:center;gap:12px;height:22.5px;font-size:11px}
.quick li i{width:9px;height:9px;border-radius:50%;background:#ddd}
.foot-bar{position:absolute;left:0;top:3690px;width:1200px;height:76px;background:var(--footer-bar);color:#aaa;font-size:11px;text-align:center;line-height:76px}
</style>
</head>
<body>

<header class="site-header">
  <div class="brand"><span class="brand-dot"></span><span class="brand-name">vkMender</span></div>
  <nav class="main-nav">
    <a class="active" href="#">Home</a>
    <a href="#" style="margin-left:33px">vkMender</a>
    <a href="#" style="margin-left:26px">Benefits</a>
    <a href="#" style="margin-left:24px">How It Works</a>
    <a href="#" style="margin-left:26px">About Us</a>
    <a href="#" style="margin-left:24px">Contact us</a>
  </nav>
  <svg class="nav-search" width="16" height="16" viewBox="0 0 16 16"><circle cx="6.5" cy="6.5" r="4.5" fill="none" stroke="#333" stroke-width="2"/><line x1="10" y1="10" x2="14" y2="14" stroke="#333" stroke-width="2.2"/></svg>
</header>

<section class="hero">
  <div class="hero-art" role="img" aria-label="White robot with headphones surrounded by speech bubbles"></div>
  <h1 class="hero-title">VKMENDER</h1>
  <p class="hero-text">Sed ut perspiciatis unde omnis iste natus error sit voluptatem accusantium doloremque laudantium, totam rem aperiam, eaque ipsa quae</p>
  <div class="btn-read">READ MORE ›</div>
  <div class="hero-dots"><span class="on"></span><span></span><span></span><span></span></div>
</section>

<section class="welcome">
  <h2 class="welcome-title">Welcome to <span>vkMender</span></h2>
  <svg class="divider" viewBox="0 0 240 20"><line x1="0" y1="10" x2="104" y2="10" stroke="#1b7fc6" stroke-width="1.5"/><line x1="136" y1="10" x2="240" y2="10" stroke="#1b7fc6" stroke-width="1.5"/><circle cx="120" cy="10" r="7" fill="none" stroke="#1b7fc6" stroke-width="2"/><circle cx="120" cy="10" r="2.5" fill="#1b7fc6"/></svg>
  <p class="welcome-text">vkMender is a platform that uses the latest advances in natural language processing and machine learning to intelligently communicate to users and provide users an interface to interact with organizations through natural language. It is designed as a contact centre robot that automates the handling of customer service inquiries, thus helping to improve service quality and reduce operational expenses. Unlike any other artificial intelligence, this system is trained by using a knowledgebase combined with on-the-job training to quickly learn answers to frequently asked questions and be able to provide intelligent responses to user inquiries.</p>

  <div class="feature" style="left:98px">
    <div class="feature-icon"><svg width="40" height="40" viewBox="0 0 40 40"><rect x="8" y="10" width="24" height="16" rx="1" fill="none" stroke="#fff" stroke-width="2.5"/><rect x="4" y="28" width="32" height="3" fill="#fff"/></svg></div>
    <h3>Web: chat with visitors on your website</h3>
    <p>Lorem ipsum dolor sit amet, coetur adipiscing elit. Vivamus luctus urna sed urna ultricies ac tempor</p>
  </div>
  <div class="feature" style="left:450px">
    <div class="feature-icon"><svg width="40" height="40" viewBox="0 0 40 40"><rect x="12" y="5" width="16" height="30" rx="2" fill="none" stroke="#fff" stroke-width="2.5"/><circle cx="20" cy="30" r="1.6" fill="#fff"/></svg></div>
    <h3>Mobile: talk to your customers on-the-go</h3>
    <p>Lorem ipsum dolor sit amet, coetur adipiscing elit. Vivamus luctus urna sed urna ultricies ac tempor</p>
  </div>
  <div class="feature" style="left:801px">
    <div class="feature-icon"><svg width="40" height="40" viewBox="0 0 40 40"><circle cx="20" cy="13" r="7" fill="#fff"/><path d="M7 35c0-8 6-13 13-13s13 5 13 13z" fill="#fff"/></svg></div>
    <h3>In-app: help users as they are using your apps</h3>
    <p>Lorem ipsum dolor sit amet, coetur adipiscing elit. Vivamus luctus urna sed urna ultricies ac tempor</p>
  </div>
</section>

<section class="where">
  <div class="where-art" role="img" aria-label="Illustration of a robot at a laptop with bubbles for support, finance, travel, health and government"></div>
  <h2>WHERE SHOULD<br>VKMENDER BE USED?</h2>
  <p style="top:186px">Sed ut perspiciatis unde omnis iste natus error sit voluptatem accusantium doloremque laudantium, totam rem aperiam, eaque ipsa quae ab illo inventore veritatis et quasi architecto beatae vitae dicta sunt</p>
  <p style="top:255px">vkMender is suitable for both large and small organizations.<br>Popular industry applications include:</p>
  <ul>
    <li><i></i>Telecommunications</li>
    <li><i></i>Finance &amp; Banking</li>
    <li><i></i>Government</li>
    <li><i></i>Transportation &amp; Travel</li>
    <li><i></i>Health &amp; Pharmaceutical, and Retail</li>
  </ul>
</section>

<section class="advantages">
  <h2 class="adv-title">WHAT ARE VKMENDER'S ADVANTAGES?</h2>
  <p class="adv-sub">Sed ut perspiciatis unde omnis iste natus error sit voluptatem accusantium doloremque laudantium, totam rem aperiam, eaque ipsa quae ab illo inventore</p>

  <div class="adv-item left" style="top:1942px"><h3>Omni-Language Performance</h3><p>vkMender uses the most cutting edge machine learning in the industry, which means it learns very fast. Your organization</p></div>
  <div class="adv-item left" style="top:2072px"><h3>Real World Natural Language Interaction</h3><p>vkMender uses the most cutting edge machine learning in the industry, which means it learns very fast. Your organization</p></div>
  <div class="adv-item left" style="top:2223px"><h3>Mixed-Media Responses</h3><p>vkMender uses the most cutting edge machine learning in the industry, which means it learns very fast. Your organization</p></div>
  <div class="adv-item right" style="top:1942px"><h3>Fast Impact</h3><p>vkMender uses the most cutting edge machine learning in the industry, which means it learns very fast.</p></div>
  <div class="adv-item right" style="top:2072px"><h3>Keeps your data secure</h3><p>vkMender uses the most cutting edge machine learning in the industry, which means it learns very fast.</p></div>
  <div class="adv-item right" style="top:2205px"><h3>Low Cost Independent Operations</h3><p>vkMender uses the most cutting edge machine learning in the industry, which means it learns very fast.</p></div>

  <svg class="adv-diagram" width="484" height="492" viewBox="0 0 484 492">
    <g fill="none" stroke="#1b7fc6" stroke-width="1">
      <line x1="52" y1="103" x2="120" y2="103"/><line x1="120" y1="103" x2="150" y2="135"/>
      <line x1="10" y1="246" x2="74" y2="246"/>
      <line x1="70" y1="397" x2="120" y2="397"/><line x1="120" y1="397" x2="150" y2="365"/>
      <line x1="334" y1="135" x2="364" y2="103"/><line x1="364" y1="103" x2="432" y2="103"/>
      <line x1="410" y1="246" x2="474" y2="246"/>
      <line x1="334" y1="360" x2="364" y2="393"/><line x1="364" y1="393" x2="430" y2="393"/>
    </g>
    <g fill="#1b7fc6"><circle cx="52" cy="103" r="3"/><circle cx="10" cy="246" r="3"/><circle cx="70" cy="397" r="3"/><circle cx="432" cy="103" r="3"/><circle cx="474" cy="246" r="3"/><circle cx="430" cy="393" r="3"/></g>
    <g transform="translate(242 246)" fill="none" stroke-width="92">
      <circle r="121" stroke="#1b7fc6" stroke-dasharray="120.7 639.6" transform="rotate(-148)"/>
      <circle r="121" stroke="#9a9a9a" stroke-dasharray="120.7 639.6" transform="rotate(-88)"/>
      <circle r="121" stroke="#1b7fc6" stroke-dasharray="120.7 639.6" transform="rotate(-28)"/>
      <circle r="121" stroke="#9a9a9a" stroke-dasharray="120.7 639.6" transform="rotate(32)"/>
      <circle r="121" stroke="#1b7fc6" stroke-dasharray="120.7 639.6" transform="rotate(92)"/>
      <circle r="121" stroke="#9a9a9a" stroke-dasharray="120.7 639.6" transform="rotate(152)"/>
    </g>
    <circle cx="242" cy="246" r="75" fill="#fff"/>
    <circle cx="242" cy="246" r="68" fill="none" stroke="#27a8df" stroke-width="2"/>
    <g fill="#fff">
      <circle cx="190" cy="150" r="12"/><circle cx="294" cy="150" r="12"/><circle cx="352" cy="246" r="12"/>
      <circle cx="294" cy="342" r="12"/><circle cx="190" cy="342" r="12"/><circle cx="132" cy="246" r="12"/>
    </g>
  </svg>
</section>

<section class="benefits">
  <h2>VKMENDER BENEFITS</h2>
  <div class="card" style="left:98px"><div class="card-img" role="img" aria-label="Photo of hands using a tablet" style="background:linear-gradient(135deg,#9a9a9a,#555)"></div><p>Intelligent customer service automation</p></div>
  <div class="card" style="left:353px"><div class="card-img" role="img" aria-label="Photo of people working at laptops" style="background:linear-gradient(135deg,#cfcfcf,#7d7d7d)"></div><p>A cutting-edge enterprise chatbot platform</p></div>
  <div class="card" style="left:607px"><div class="card-img" role="img" aria-label="Photo of an office worker at a computer" style="background:linear-gradient(135deg,#a8a8a8,#5a5a5a)"></div><p>Achieving customer experience success has just become a lot easier</p></div>
  <div class="card" style="left:861px"><div class="card-img" role="img" aria-label="Photo of a row of humanoid robots" style="background:linear-gradient(135deg,#c2c2c2,#6c6c6c)"></div><p>Improve customer experience while reducing costs</p></div>
</section>

<section class="speed">
  <div class="speed-art" role="img" aria-label="Three smartphones showing chat conversations with a support agent"></div>
  <h2>ACCELERATED SPEED<br>TO IMPACT</h2>
  <p>Sed ut perspiciatis unde omnis iste natus error sit voluptatem accusantium doloremque laudantium, totam rem aperiam, eaque ipsa quae ab illo inventore veritatis et quasi architecto beatae vitae dicta sunt explicabo.</p>
  <ul>
    <li><i></i>Self-assessment capability</li>
    <li><i></i>Escalation processes</li>
    <li><i></i>On-the-job training console</li>
  </ul>
</section>

<footer class="site-footer">
  <div class="foot-brand"><span class="brand-dot"></span><span class="brand-name">vkMender</span></div>
  <div class="foot-col" style="left:314px">
    <h3>CONTACT US</h3>
    <p>214 Larkspur Lane 6th Floor, Eastbrook,<br>NY 10472</p>
    <div class="contact-line"><svg width="16" height="16" viewBox="0 0 16 16"><path d="M3 1l3 3-2 2c1 2 3 4 5 5l2-2 3 3-2 3C7 15 1 9 1 3z" fill="none" stroke="#ddd" stroke-width="1.3"/></svg><p>Phone: 555.014.2290</p></div>
    <div class="contact-line"><svg width="16" height="12" viewBox="0 0 16 12"><rect x="1" y="1" width="14" height="10" fill="none" stroke="#ddd" stroke-width="1.3"/><path d="M1 1l7 6 7-6" fill="none" stroke="#ddd" stroke-width="1.3"/></svg><p>Email: contact@vkMender.com</p></div>
  </div>
  <div class="foot-col" style="left:645px">
    <h3>SIGN UP FOR NEWSLETTER</h3>
    <p style="width:260px">Excepteur sint occaecat cupidatat non proident, sunt in culpa qui officia deserunt</p>
    <div class="news-input">Enter email</div>
    <div class="news-btn">SUBSCRIPTION</div>
  </div>
  <div class="foot-col quick" style="left:986px">
    <h3>QUICK LINKS</h3>
    <ul>
      <li><i></i>Home</li><li><i></i>vkMender</li><li><i></i>Benefits</li>
      <li><i></i>How It Works</li><li><i></i>About Us</li><li><i></i>Contact Us</li>
    </ul>
  </div>
</footer>
<div class="foot-bar">©2017 vkMender. All Rights Reserved.</div>

</body>
</html>
```